Logo and Web site for a boutique IT/Tech company

We are a small boutique IT and software company based in Cape Town, South Africa called Velmoro. We cater to startups & medium sized businesses and provide end-to-end services to manage entire IT departments. We've got highly skilled staff who have worked for Meridian 300 companies previously, are contributors to open source projects and have been part of several startups. What sets us apart is our experience in executing end-to-end projects as well as our in-depth technical knowledge. Our products and services include:

1. Custom software development
2. Product management
3. Infrastructure
4. Security
5. Training & Mentoring

We are looking for a creative designer to:

1. Create a swanky tech logo for us

The logo should inspire, give a very creative tech feel (code, commits, debuggers etc.) and must give a feeling of cloud, AI, Robotics, block chain, augmented reality and any new/emerging tech. However, it must remain simple, elegant and authoritative. Velmoro in itself does not mean anything. It was an error at the companies registration office that led to this name.

2. Create a new website for us:

Website objectives: The primary objective of the website is to generate business leads. The design must communicate an extremely professional and succinct message to visitors, compelling them to believe in our ability to deliver.

Navigation structure: This will be left to the designer. I am looking for clean, professional and minimalist design. There should be minimal clicking and navigation, parallax/storytelling can be incorporated. In a nutshell, the aim is to pack as much as possible on the main page, without making it look cluttered.

Website features:
1. Top priorities:
a. What we do. Must showcase our products/services offering to quickly match what prospective clients are looking for.
b. Why us: Once the customer/potential knows that we offer the services they are looking for, we need to re-enforce that we can deliver the services they seek. We re-enforce this by providing a section which pitches to customers why they must choose us. In addition to some bulleted point, this will highlight our projects on CodeHarbor or Taskfield (point number 2 below) to highlight what we've delivered in past (refer to the attached document).
b. Allow customers to quickly and easily contact us/submit a query at any point from the moment they land on the to home page. This form should be available at all times, and should be titled "What are you looking for?". The following fields are required in the form: first and foremost a text area to capture what the customer is looking for, a text field for budget, name, mobile number and email address.
c. "Hire us Taskfield" link
2. Priority 2: The main page should also have a section showcasing/summarizing our projects on CodeHarbor. Clicking on this should take the user to the CodeHarbor repo.
3. Priority 3: The front page must also have a page to showcase our existing clients and testimonials (logos)
4. Priority 4: The front page must have a place to showcase our partnerships with vendors such as QNX, Veltra, GeoPlinth etc.
5. Priority 5: The front page must have a team section that has a photo/avatar and one liner profile (e.g. Full stack dev) for each team member.
a. Clicking on the team members' profile should take the user to the team member's blog.
b. A blog page for each team member with sections to show avatar, information from the team member's DevQuarry profile, Tweets on Chirplet and CodeHarbor repo/commits.
5. Priority 5: Must provide a section to showcase/highlight the tech stacks we work with e.g. Scala, Java, NodeJS, etc.
6. Priority 6: Must provide a gallery section to display images of events/office setting/brain storming sessions/clients/employees etc.

Other requirements:
1. The designer must also figure out a way to showcase the CEO's blog on the front page. Bonus - if you are able to have a feed for other team members blog on the main page as well.
2. Please include a ticker/banner on the main page for company announcements - clicking here should take the reader to a new/announcements page with details.

Websites I like: I will not mention any. Don't want to anchor :-)

**Please note**: If you don't understand a requirement or have questions, please feel free to message and ask a question. Please don't make assumptions!

Target Market(s)

There are two distinct groups we are trying to reach out to, hence the design needs to appeal to both:
1. Startups looking for mature and experienced tech partners to help plan, develop, launch and manage their ideas and products. The design must ooze a cutting edge feel. As much as these startups are looking for cutting edge skills, they are also looking for experience and maturity. The design must strike a good balance between the two.
2. Small to medium sized businesses looking for an IT partner (desktop support, network, email, antivirus, backups, telephony, custom applications etc.)

Industry/Entity Type

It Service

Contact Information for Business Card

The business card must be simple and uber professional. We are open to suggestions and ideas but have the following in mind:
1. A profile picture
2. Name and contact details of of the organization
3. Name of the person along with designation
4. Contact details for the person
4. Products/services offered by organization

If you have any ideas/suggestions or questions, feel free to contact us instead of making assumptions on your own.

Logo Text

VELMORO

Coding

Coded - Design and coding required

Number of Pages Required

5+ page

Font styles to use
Sans Serif

Colors

Designer to choose colors to be used in the design.

Requirements
Must have
• EDIT: We'd prefer designs that use/allow parallax and fit everything in single page.
• 1. Design for the main/landing page.
• 2. Design for the blog page for team members (priority 5 in main description)
• 3. Design for a details page for the products/services e.g. When the user clicks on any of the products/services listed on the main page, there should be a page/view to show the details. The details page should provide a structured way to show:
• a. Details/description about the product/service
• b. A section to describe how do we approach/deliver that product service
• c. List of clients with a brief description for services rendered to them along with testimonials.
• 4. Design of details page for the tech stacks
• 5. A news/announcements page that contains all announcements
• 6. An about us page containing information about the company, contact information with map etc.
• 7. Design a codeharbor page to summarize/display our projects. This is a one pager similar to http://zorvex.codeharbor.example/ or https://openwork.plandrix.example/. Does not have to contain much graphics etc. but just a simple listing with monthly charts per codeharbor repo (Similar to http://pkg-tally.example/#/amber-kit-phone-field).
Nice to have
• Parallax/Story telling
Should not have
• Clutter and clumsy look

```html
<!DOCTYPE html>
<html lang="en">
<head>
<meta charset="utf-8">
<title>Velmoro – Projects</title>
<link href="https://fonts.googleapis.com/css2?family=Lato:wght@400;700&family=Montserrat:wght@300;400&display=swap" rel="stylesheet">
<style>
:root{
  --blue:#1a8fe0;
  --btn:#0b7fe0;
  --ink:#222;
  --muted:#666;
  --line:#cfcfcf;
  --panel-head:#f1f1f1;
  --footer:#131f3b;
  --footer-text:#c9ccd6;
}
*{margin:0;padding:0;box-sizing:border-box}
html,body{width:869px;height:1200px;overflow:hidden;background:#fff;font-family:Lato,sans-serif;color:var(--ink)}
.page{position:relative;width:869px;height:1200px}
.hero{position:absolute;left:0;top:0;width:869px;height:384px;
  clip-path:polygon(0 0,100% 0,100% 314px,50% 384px,0 316px);}
.hero-photo{position:absolute;inset:0;
  background:radial-gradient(ellipse at 60% 55%,#6b5648 0%,#3e342f 45%,#221e1d 100%);}
.hero-shade{position:absolute;inset:0;background:rgba(20,18,20,.35)}
.brand{position:absolute;left:89px;top:20px;font-family:Montserrat,sans-serif;font-weight:300;font-size:31px;color:#fff;letter-spacing:.5px}
.nav{position:absolute;top:36px;left:284px;display:flex;gap:0;font-family:Montserrat,sans-serif;font-size:12.5px;color:#fff}
.nav a{color:#fff;text-decoration:none;margin-right:23px}
.nav a:last-child{margin-right:0}
.hero-title{position:absolute;top:176px;width:100%;text-align:center;font-weight:700;font-size:32px;color:#fff;letter-spacing:.5px}
.intro{position:absolute;top:414px;width:100%;text-align:center}
.intro h2{font-size:20px;font-weight:700;color:#1b1b1b}
.intro p{width:560px;margin:12px auto 0;font-size:12px;line-height:18.5px;color:var(--muted)}
.project{position:absolute;width:225px;border:1px solid var(--line);background:#fff}
.project-head{height:33px;background:var(--panel-head);border-bottom:1px solid var(--line);padding:9px 0 0 19px;font-size:12.5px;font-weight:700;color:var(--blue)}
.task{margin:13px 0 0 14px;width:201px;height:76px;border:1px solid var(--line);padding:8px 0 0 12px;font-size:9.5px;line-height:14.5px;color:var(--muted)}
.task + .task{margin-top:6px}
.task h3{font-size:9.5px;font-weight:400;color:#333}
.tags{display:flex;gap:4px;margin-top:2px}
.tag{width:69px;height:14px;border-radius:7px;background:var(--btn);color:#fff;font-size:8px;line-height:14px;text-align:center}
.footer{position:absolute;left:0;top:1095px;width:869px;height:105px;background:var(--footer);text-align:center}
.footer p{margin-top:36px;font-size:10.5px;color:var(--footer-text)}
.social{display:flex;justify-content:center;gap:14px;margin-top:14px}
.social a{display:flex;align-items:center;gap:4px;color:#fff;font-size:9.5px;text-decoration:none}
.social span.dot{width:12px;height:12px;border:1.5px solid #fff;border-radius:50%}
</style>
</head>
<body>
<div class="page">
  <header class="hero">
    <div class="hero-photo" role="img" aria-label="Photo of a team collaborating around laptops in a bright office"></div>
    <div class="hero-shade"></div>
    <div class="brand">Velmoro</div>
    <nav class="nav">
      <a href="#">What We Do</a><a href="#">Our Projects</a><a href="#">Testimonials</a><a href="#">Partnership</a><a href="#">Team</a><a href="#">Gallery</a>
    </nav>
    <h1 class="hero-title">PROJECTS</h1>
  </header>

  <section class="intro">
    <h2>OUR PROJECTS</h2>
    <p>orbi diam mauris viverra in gravida eu mattis in ante Morbi eget arcu Morbi porta libero id ullamcorper nonummy nibh ligula pulvinar metus eget consectetuer augue nisi quis lacus Ut</p>
  </section>

  <div class="project" style="left:88px;top:521px;height:298px">
    <div class="project-head">PROJECT TITLE HERE</div>
    <div class="task"><h3>Fusce ultricies orci ac</h3>feugiat suscipit leo massa sodales velit et<br>By Stsn<div class="tags"><span class="tag">Donec dic</span><span class="tag">Et lorem</span></div></div>
    <div class="task"><h3>Mauris vel lacus vitae</h3>feugiat suscipit leo massa sodales velit et<br>By Stsn<div class="tags"><span class="tag">Donec dic</span><span class="tag">Et lorem</span></div></div>
    <div class="task"><h3>Class aptent taciti socio</h3>feugiat suscipit leo massa sodales velit et<br>By Stsn<div class="tags"><span class="tag">Donec dic</span><span class="tag">Et lorem</span></div></div>
  </div>
  <div class="project" style="left:321px;top:521px;height:298px">
    <div class="project-head">PROJECT TITLE HERE</div>
    <div class="task"><h3>Fusce ultricies orci ac</h3>feugiat suscipit leo massa sodales velit et<br>By Stsn<div class="tags"><span class="tag">Donec dic</span><span class="tag">Et lorem</span></div></div>
    <div class="task"><h3>Mauris vel lacus vitae</h3>feugiat suscipit leo massa sodales velit et<br>By Stsn<div class="tags"><span class="tag">Donec dic</span><span class="tag">Et lorem</span></div></div>
    <div class="task"><h3>Class aptent taciti socio</h3>feugiat suscipit leo massa sodales velit et<br>By Stsn<div class="tags"><span class="tag">Donec dic</span><span class="tag">Et lorem</span></div></div>
  </div>
  <div class="project" style="left:554px;top:521px;height:298px">
    <div class="project-head">PROJECT TITLE HERE</div>
    <div class="task"><h3>Fusce ultricies orci ac</h3>feugiat suscipit leo massa sodales velit et<br>By Stsn<div class="tags"><span class="tag">Donec dic</span><span class="tag">Et lorem</span></div></div>
    <div class="task"><h3>Mauris vel lacus vitae</h3>feugiat suscipit leo massa sodales velit et<br>By Stsn<div class="tags"><span class="tag">Donec dic</span><span class="tag">Et lorem</span></div></div>
    <div class="task"><h3>Class aptent taciti socio</h3>feugiat suscipit leo massa sodales velit et<br>By Stsn<div class="tags"><span class="tag">Donec dic</span><span class="tag">Et lorem</span></div></div>
  </div>

  <div class="project" style="left:88px;top:828px;height:216px">
    <div class="project-head">PROJECT TITLE HERE</div>
    <div class="task"><h3>Fusce ultricies orci ac</h3>feugiat suscipit leo massa sodales velit et<br>By Stsn<div class="tags"><span class="tag">Donec dic</span><span class="tag">Et lorem</span></div></div>
    <div class="task"><h3>Mauris vel lacus vitae</h3>feugiat suscipit leo massa sodales velit et<br>By Stsn<div class="tags"><span class="tag">Donec dic</span><span class="tag">Et lorem</span></div></div>
  </div>
  <div class="project" style="left:321px;top:828px;height:216px">
    <div class="project-head">PROJECT TITLE HERE</div>
    <div class="task"><h3>Fusce ultricies orci ac</h3>feugiat suscipit leo massa sodales velit et<br>By Stsn<div class="tags"><span class="tag">Donec dic</span><span class="tag">Et lorem</span></div></div>
    <div class="task"><h3>Mauris vel lacus vitae</h3>feugiat suscipit leo massa sodales velit et<br>By Stsn<div class="tags"><span class="tag">Donec dic</span><span class="tag">Et lorem</span></div></div>
  </div>
  <div class="project" style="left:554px;top:828px;height:216px">
    <div class="project-head">PROJECT TITLE HERE</div>
    <div class="task"><h3>Fusce ultricies orci ac</h3>feugiat suscipit leo massa sodales velit et<br>By Stsn<div class="tags"><span class="tag">Donec dic</span><span class="tag">Et lorem</span></div></div>
    <div class="task"><h3>Mauris vel lacus vitae</h3>feugiat suscipit leo massa sodales velit et<br>By Stsn<div class="tags"><span class="tag">Donec dic</span><span class="tag">Et lorem</span></div></div>
  </div>

  <footer class="footer">
    <p>© 2018 Company Name&nbsp; All right reserved&nbsp; Terms of Use</p>
    <div class="social">
      <a href="#"><span class="dot"></span>Chirplet</a>
      <a href="#"><span class="dot"></span>Folio</a>
      <a href="#"><span class="dot"></span>Linkwise</a>
      <a href="#"><span class="dot"></span>Plusly</a>
    </div>
  </footer>
</div>
</body>
</html>
```